TRU PEAK POWER.

I'd like my business logo.
contact name: Desmond Halvik
phone:0438275160
email: info@trupeakpower.net.au
website: www.trupeakpower.net.au

services:
solar
battery storage
LED lighting
energy saving solutions
general electrical
I'd like the design to look professional

Target Market(s)

Everyone

Industry/Entity Type

Business

Contact Information for Business Card

as described above

Requirements
Must have
• Id like the colours and the design to work well with my logo.

```html
<!DOCTYPE html>
<html lang="en">
<head>
<meta charset="utf-8">
<title>Tru Peak Power – Business Cards</title>
<link rel="stylesheet" href="https://fonts.googleapis.com/css2?family=Lato:wght@400;700;900&display=swap">
<style>
  :root {
    --bg: #e3e3e3;
    --paper: #ffffff;
    --green: #76b743;
    --green-deep: #3d9f55;
    --orange: #f6901e;
    --shadow: rgba(0,0,0,0.28);
  }
  * { box-sizing: border-box; margin: 0; padding: 0; }
  html, body {
    width: 1200px; height: 900px; overflow: hidden;
    background: var(--bg);
    font-family: "Lato", sans-serif;
  }
  .stage { position: relative; width: 1200px; height: 900px; }

  .card {
    position: absolute;
    width: 560px; height: 320px;
    background: var(--paper);
    box-shadow: 4px 6px 10px var(--shadow);
  }
  .card--green-frame { left: 30px; top: 50px; border: 16px solid var(--green); }
  .card--orange-sides { left: 610px; top: 220px; border-left: 16px solid var(--orange); border-right: 20px solid var(--orange); }
  .card--split-frame {
    left: 320px; top: 565px;
    border-top: 14px solid var(--orange); border-left: 16px solid var(--orange);
    border-right: 14px solid var(--green); border-bottom: 14px solid var(--green);
  }

  .brand {
    position: absolute; left: 34px; top: 38px;
    display: flex; align-items: center; gap: 18px;
  }
  .brand__dot {
    width: 74px; height: 74px; border-radius: 50%;
    background: var(--orange);
  }
  .brand__name {
    font-weight: 900; font-size: 46px; line-height: 1;
    color: var(--green-deep); letter-spacing: -0.5px;
  }

  .services {
    position: absolute; right: 22px; top: 152px;
    list-style: none; text-align: right;
    font-weight: 900; font-size: 15.5px; line-height: 1.05;
    text-transform: uppercase; color: var(--green);
  }
  .services--orange { color: var(--orange); }
  .services .is-orange { color: var(--orange); }
  .services .is-green { color: var(--green-deep); }

  .contact {
    position: absolute; left: 42px; bottom: 26px;
    font-size: 15px; line-height: 1.2; color: var(--green);
  }
  .contact--orange { color: var(--orange); }
  .contact__name { font-weight: 700; font-size: 18px; margin-bottom: 2px; }
  .contact__line { display: flex; align-items: center; gap: 6px; }
  .contact__icon { width: 13px; height: 13px; flex: none; }
  .contact--orange .contact__name,
  .card--split-frame .contact__name { color: var(--orange); }
</style>
</head>
<body>
<svg width="0" height="0" style="position:absolute" aria-hidden="true">
  <symbol id="icon-phone" viewBox="0 0 16 16"><path fill="currentColor" d="M4 1l3 3-1.6 1.8c.8 1.9 2.4 3.6 4.6 4.6L11.8 8.8 15 12l-2 2.6C7.5 14 2 8.5 1.4 3z"/></symbol>
  <symbol id="icon-mail" viewBox="0 0 16 16"><rect x="1" y="3" width="14" height="10" fill="none" stroke="currentColor" stroke-width="1.6"/><path d="M1 3l7 6 7-6" fill="none" stroke="currentColor" stroke-width="1.6"/></symbol>
  <symbol id="icon-globe" viewBox="0 0 16 16"><g fill="none" stroke="currentColor" stroke-width="1.3"><circle cx="8" cy="8" r="6.5"/><ellipse cx="8" cy="8" rx="3" ry="6.5"/><path d="M1.5 8h13M2.5 4.8h11M2.5 11.2h11"/></g></symbol>
</svg>

<main class="stage">
  <!-- Green-framed card -->
  <article class="card card--green-frame">
    <div class="brand"><span class="brand__dot"></span><span class="brand__name">Tru Peak Power</span></div>
    <ul class="services">
      <li>Solar</li><li>Battery Storage</li><li>LED Lighting</li><li>Energy Saving Solutions</li>
    </ul>
    <div class="contact">
      <p class="contact__name">Desmond Halvik</p>
      <p class="contact__line"><svg class="contact__icon"><use href="#icon-phone"/></svg>0438275160</p>
      <p class="contact__line"><svg class="contact__icon"><use href="#icon-mail"/></svg>info@trupeakpower.net.au</p>
      <p class="contact__line"><svg class="contact__icon"><use href="#icon-globe"/></svg>www.trupeakpower.net.au</p>
    </div>
  </article>

  <!-- Orange-sided card -->
  <article class="card card--orange-sides">
    <div class="brand"><span class="brand__dot"></span><span class="brand__name">Tru Peak Power</span></div>
    <ul class="services services--orange">
      <li>Solar</li><li>Battery Storage</li><li>LED Lighting</li><li>Energy Saving Solutions</li>
    </ul>
    <div class="contact contact--orange">
      <p class="contact__name">Desmond Halvik</p>
      <p class="contact__line"><svg class="contact__icon"><use href="#icon-phone"/></svg>0438275160</p>
      <p class="contact__line"><svg class="contact__icon"><use href="#icon-mail"/></svg>info@trupeakpower.net.au</p>
      <p class="contact__line"><svg class="contact__icon"><use href="#icon-globe"/></svg>www.trupeakpower.net.au</p>
    </div>
  </article>

  <!-- Orange and green split-frame card -->
  <article class="card card--split-frame">
    <div class="brand"><span class="brand__dot"></span><span class="brand__name">Tru Peak Power</span></div>
    <ul class="services">
      <li class="is-orange">Solar</li><li class="is-green">Battery Storage</li><li class="is-orange">LED Lighting</li><li class="is-green">Energy Saving Solutions</li>
    </ul>
    <div class="contact">
      <p class="contact__name">Desmond Halvik</p>
      <p class="contact__line"><svg class="contact__icon"><use href="#icon-phone"/></svg>0438275160</p>
      <p class="contact__line"><svg class="contact__icon"><use href="#icon-mail"/></svg>info@trupeakpower.net.au</p>
      <p class="contact__line"><svg class="contact__icon"><use href="#icon-globe"/></svg>www.trupeakpower.net.au</p>
    </div>
  </article>
</main>
</body>
</html>
```